Funky Retro Membership Brochure

We require an A5 (A4 folded) brochure design that outlines the membership options for FernLoop. FernLoop promotes local businesses via social media and presence on the FernLoop website (www.fernloop-example.com.au) as well as providing networking facilities for the local business to meet and collaborate with each other.

Attached are the various Fernloop logos together with the colour style guide. Please ignore the fonts; just note the colours.

We would like the brochure to have a retro style look. Very funky but professional.

The first page of the brochure is the title page. Logo with the following tagline "Linking and Lifting Local Trade across Sydney's Inner West". Additional Text, "2020 Membership". Please also include"#fernloop" on the title page. This hashtag should be in a retro font on an angle.

The second page refers to what we do. Three section headings and text as follows but will require designers to provide appropriate graphics, for example the FernLoop website inside a computer screen etc.:

FERNLOOP WEBSITE
fernloop-example.com.au is the online, digital showcase of our members and their business. Each member has a dedicated webpage to promote their business. Your member page provides all you contact details, links and social media channels, reviews, logos and more.

GUMNOOK
GumNook is where FernLoop members get together. It’s a business community unlike any other. No selling. No Pressure. And it won’t break the bank. We aim to stop the isolation many business owners feel and encourage genuine connections, where referrals happen naturally.

SOCIAL MEDIA
FernLoop uses social media channels to actively promote the FernLoop community and its members. Not only do we promote the businesses but also provide free promotions and advertising for local community groups, schools and non-for-profit organisations.

The third page provides details of the membership levels and annual fees. The information on the membership categories can be found at https://www.fernloop-example.com.au/membership-levels/ All the information contained on the page should be contained on page three of the brochure.

The final, back page, will contain all of the contact details for FernLoop (also found on the www.fernloop-example.com.au)

Target Market(s)

Local community businesses

Industry/Entity Type

Digital Marketing

Font styles to use
Other font styles liked:
• Retro

Requirements
Must have
• Retro feel - refer to project description
Nice to have
• Refer to project description
Should not have
• Not applicable

```html
<!DOCTYPE html>
<html lang="en">
<head>
<meta charset="utf-8">
<title>FernLoop 2020 Membership Brochure</title>
<link rel="stylesheet" href="https://fonts.googleapis.com/css2?family=Bebas+Neue&family=Playfair+Display:ital,wght@1,700&family=Roboto:wght@500&display=swap">
<style>
  :root {
    --frame-blue: #5b9bbf;
    --headline-blue: #5b9bbf;
    --slate: #4e5a6e;
    --paper-light: #f2e3d3;
    --paper-mid: #e3cdb7;
    --paper-dark: #cfb49a;
    --logo-grey: #8a8f9c;
    --white: #ffffff;
  }
  * { margin: 0; padding: 0; box-sizing: border-box; }
  html, body { width: 1200px; height: 851px; overflow: hidden; background: var(--frame-blue); }
  .spread { position: relative; width: 1200px; height: 851px; background: var(--frame-blue); }
  .panel { position: absolute; top: 0; width: 597px; height: 851px; overflow: hidden; }
  .panel--back { left: 0; }
  .panel--cover { left: 603px; }
  .panel__photo {
    position: absolute; inset: 12px;
    background: radial-gradient(ellipse at 50% 45%, var(--paper-light) 0%, var(--paper-mid) 60%, var(--paper-dark) 100%);
  }
  .logo { position: absolute; display: flex; align-items: center; gap: 10px; }
  .logo__mark { width: 62px; height: 62px; border-radius: 50%; border: 7px solid var(--white); }
  .logo__name { font-family: "Roboto", sans-serif; font-weight: 500; font-size: 34px; color: var(--logo-grey); letter-spacing: 0.5px; }
  .panel--back .logo { left: 196px; top: 32px; }
  .panel--cover .logo { left: 187px; top: 22px; }

  .intro {
    position: absolute; left: 30px; top: 124px; width: 540px; text-align: center;
    font-family: "Playfair Display", serif; font-style: italic; font-weight: 700;
    text-transform: uppercase; color: var(--headline-blue); font-size: 20px; line-height: 40px;
  }
  .contact-title {
    position: absolute; left: 0; width: 597px; top: 418px; text-align: center;
    font-family: "Bebas Neue", sans-serif; font-size: 58px; color: var(--headline-blue); line-height: 1;
  }
  .contact-box {
    position: absolute; left: 78px; top: 508px; width: 468px; height: 190px;
    background: rgba(255,255,255,0.6); padding: 14px 10px; display: flex; flex-direction: column; justify-content: space-between;
  }
  .contact-item { display: flex; align-items: center; gap: 6px; font-family: "Bebas Neue", sans-serif; font-size: 16px; color: var(--slate); letter-spacing: 0.3px; }
  .contact-item__icon { width: 19px; height: 19px; border-radius: 3px; flex: none; display: flex; align-items: center; justify-content: center; }
  .icon--social { background: var(--frame-blue); }
  .icon--alt { background: #b9505a; }

  .tagline { position: absolute; left: 0; width: 597px; top: 150px; text-align: center; font-family: "Bebas Neue", sans-serif; line-height: 1; }
  .tagline__line { display: block; font-size: 62px; height: 76px; }
  .tagline__line--blue { color: var(--headline-blue); }
  .tagline__line--slate { color: var(--slate); }
  .membership-badge {
    position: absolute; left: 117px; top: 581px; width: 359px; height: 63px;
    border: 2px solid var(--slate); background: rgba(255,255,255,0.75);
    clip-path: polygon(4% 0, 96% 0, 100% 50%, 96% 100%, 4% 100%, 0 50%);
    display: flex; align-items: center; justify-content: center;
    font-family: "Playfair Display", serif; font-style: italic; font-weight: 700; font-size: 30px; color: var(--slate);
  }
  .hashtag-ribbon {
    position: absolute; right: -60px; bottom: 38px; width: 260px; height: 34px; transform: rotate(-45deg);
    background: var(--white); text-align: center; font-family: "Bebas Neue", sans-serif; font-size: 30px; line-height: 36px; color: var(--slate);
  }
</style>
</head>
<body>
<main class="spread">
  <section class="panel panel--back">
    <div class="panel__photo" role="img" aria-label="Sepia photograph of vintage telephone handsets hanging on cords"></div>
    <div class="logo"><span class="logo__mark"></span><span class="logo__name">FERN LOOP</span></div>
    <p class="intro">When you advertise your business with<br>FernLoop you become part of a community<br>of likeminded businesses owners.</p>
    <h2 class="contact-title">Contact Us</h2>
    <ul class="contact-box">
      <li class="contact-item"><span class="contact-item__icon icon--social"></span>https://social-one.example/fernloopinnerwest</li>
      <li class="contact-item"><span class="contact-item__icon icon--social"></span>https://social-two.example/fernloop_innerwest/</li>
      <li class="contact-item"><span class="contact-item__icon icon--alt"></span>https://video-hub.example/channel/fernloop-inner-west</li>
      <li class="contact-item"><span class="contact-item__icon icon--social"><svg width="13" height="13" viewBox="0 0 24 24"><path fill="#222" d="M6.6 10.8a15 15 0 0 0 6.6 6.6l2.2-2.2c.3-.3.7-.4 1-.2 1.1.4 2.3.6 3.6.6.6 0 1 .4 1 1V20c0 .6-.4 1-1 1A17 17 0 0 1 3 4c0-.6.4-1 1-1h3.5c.6 0 1 .4 1 1 0 1.3.2 2.5.6 3.6.1.3 0 .7-.2 1z"/></svg></span>Phone: 0400 182 650</li>
      <li class="contact-item"><span class="contact-item__icon icon--alt"><svg width="13" height="13" viewBox="0 0 24 24"><text x="12" y="18" text-anchor="middle" font-size="18" fill="#fff" font-family="sans-serif">@</text></svg></span>Email: chat@fernloop-example.com.au</li>
    </ul>
  </section>

  <section class="panel panel--cover">
    <div class="panel__photo" role="img" aria-label="Sepia photograph of several vintage telephone handsets hanging on cords"></div>
    <div class="logo"><span class="logo__mark"></span><span class="logo__name">FERN LOOP</span></div>
    <h1 class="tagline">
      <span class="tagline__line tagline__line--blue">Linking</span>
      <span class="tagline__line tagline__line--slate">and</span>
      <span class="tagline__line tagline__line--blue">Lifting</span>
      <span class="tagline__line tagline__line--slate">Local Trade across</span>
      <span class="tagline__line tagline__line--blue">Sydney’s Inner West</span>
    </h1>
    <div class="membership-badge">2020 Membership</div>
    <div class="hashtag-ribbon">#FERNLOOP</div>
  </section>
</main>
</body>
</html>
```